Design a DL flyer double sided 4 colour 210mm x 95 mm (portrait) for the launch of a new yoga studio opening in North Melbourne on the 23 November 2013.
The final design should communicate with a strong call to action- the opening date , register to receive your first class free and like us on Friendsphere.
The studio provides a tranquil, open space to practice yoga, create a feeling of light, peace and a nurturing environment, please create this feeling in the design.

An example design mock (rough design feel free to move around as required, includes final content) print specifications, logo, typography style and image attached.
The reverse side to include logo, address and please design the timetable for the launch week (refer design mock)
Have also attached a reverse logo for a dark background and are open to designer providing examples with various background colours and effects.
Back content can be moved to the front side if required to facilitate design

Target Market(s)

People in the area who are practicing yoga elsewhere and encourage them to come to the studio to try us out with a free opening offer in our first week. And people new to yoga wanting to give it a try.
Experienced yoga people and people new to yoga - all ages

Industry/Entity Type

Environment

Requirements
Must have
• The Calm Haven logo physical address, website address, the tagline live, breathe, love...
The final design should communicate with a strong call to action- the opening date , register to receive your first class free and like us on Friendsphere. and the website address thecalmhaven.com.au, drive them to the website to register.
The studio provides a tranquil, open space to practice yoga, create a feeling of light, peace and a nurturing environment, please create this feeling in the design

```html
<!DOCTYPE html>
<html lang="en">
<head>
<meta charset="utf-8">
<title>The Calm Haven – Studio Opening Flyer</title>
<link rel="stylesheet" href="https://fonts.googleapis.com/css2?family=Noto+Sans:wght@400;700&display=swap">
<style>
  :root {
    --leaf-green: #5cb82a;
    --leaf-green-deep: #54aa25;
    --page-bg: #e4e4e2;
    --photo-canopy: #8fb13a;
    --photo-foliage: #b4c253;
    --photo-light: #d8d49a;
    --photo-floor: #dcd8c4;
    --veil: rgba(190, 190, 176, 0.55);
    --ink-light: #ffffff;
  }
  html, body {
    margin: 0;
    padding: 0;
    width: 1200px;
    height: 1200px;
    overflow: hidden;
    background: var(--page-bg);
    font-family: "Noto Sans", Tahoma, sans-serif;
  }
  .flyer {
    position: absolute;
    left: 330px;
    top: 47px;
    width: 540px;
    height: 1106px;
    overflow: hidden;
    background: var(--leaf-green);
    box-shadow: 0 6px 24px rgba(0, 0, 0, 0.18);
    color: var(--ink-light);
  }
  .studio-photo {
    position: absolute;
    left: 0;
    top: 0;
    width: 100%;
    height: 680px;
    background:
      radial-gradient(ellipse 70% 40% at 75% 30%, rgba(216, 212, 154, 0.7) 0%, rgba(216, 212, 154, 0) 70%),
      radial-gradient(ellipse 60% 35% at 15% 40%, rgba(143, 177, 58, 0.8) 0%, rgba(143, 177, 58, 0) 70%),
      linear-gradient(180deg, var(--photo-canopy) 0%, var(--photo-foliage) 40%, var(--photo-light) 70%, var(--photo-floor) 100%);
  }
  .brand-band {
    position: absolute;
    left: 0;
    top: 55px;
    width: 100%;
    height: 100px;
    background: var(--leaf-green);
    text-align: center;
  }
  .brand-name {
    display: inline-flex;
    align-items: center;
    gap: 12px;
    margin-top: 14px;
    font-size: 38px;
    font-weight: 700;
    line-height: 1;
    letter-spacing: -0.5px;
  }
  .brand-dot {
    width: 30px;
    height: 30px;
    border-radius: 50%;
    background: var(--ink-light);
  }
  .tagline {
    margin: 8px 70px 0 0;
    font-size: 21px;
    font-weight: 400;
    text-align: right;
  }
  .offer-veil {
    position: absolute;
    left: 0;
    top: 275px;
    width: 100%;
    height: 205px;
    background: var(--veil);
    text-align: center;
  }
  .opening-title {
    margin: 34px 0 0;
    font-size: 33px;
    font-weight: 400;
    line-height: 1.1;
  }
  .opening-date {
    margin: 0;
    font-size: 25px;
    font-weight: 400;
  }
  .offer-title {
    margin: 24px 0 0;
    font-size: 25px;
    font-weight: 400;
  }
  .offer-dates {
    margin: 0;
    font-size: 20px;
    font-weight: 400;
  }
  .booking-panel {
    position: absolute;
    left: 0;
    top: 676px;
    width: 100%;
    height: 430px;
    background: linear-gradient(180deg, var(--leaf-green) 0%, var(--leaf-green-deep) 100%);
    text-align: center;
  }
  .booking-copy {
    margin: 72px 14px 0;
    font-size: 28px;
    font-weight: 400;
    line-height: 1.5;
    white-space: nowrap;
  }
</style>
</head>
<body>
  <main class="flyer">
    <div class="studio-photo" role="img" aria-label="Sunlit yoga studio interior opening onto green trees"></div>

    <header class="brand-band">
      <div class="brand-name"><span class="brand-dot"></span>The Calm Haven</div>
      <p class="tagline">Live, Breathe, Love</p>
    </header>

    <section class="offer-veil">
      <h1 class="opening-title">New Yoga Studio Opening</h1>
      <p class="opening-date">23 November</p>
      <h2 class="offer-title">First Class Free in Opening Week</h2>
      <p class="offer-dates">Opening Week 23 Nov - Nov 29</p>
    </section>

    <section class="booking-panel">
      <p class="booking-copy">
        To book your FREE class go<br>
        online to register and book, like<br>
        us on Friendsphere<br>
        <span class="studio-location">The Calm Haven - Melbourne</span><br>
        View other Opening Specials at<br>
        thecalmhaven.com.au
      </p>
    </section>
  </main>
</body>
</html>
```